Brindle Sky Advisory needs a wordpress design

New consulting company based in San Francisco focusing on leading businesses (primarily startups) into the cloud. Services include: cloud architecture, security, automation, back-end design, Infrastructure Optimization, Capacity Planning. Even though we are a new company, I'd like to convey a sense of confidence to the prospective client. Logos are attached

Target Market(s)

Start-ups looking to move their application into the cloud

Industry/Entity Type

Information Technology

```html
<!DOCTYPE html>
<html lang="en">
<head>
<meta charset="utf-8">
<title>Brindle Sky Advisory</title>
<link rel="stylesheet" href="https://fonts.googleapis.com/css2?family=Open+Sans:wght@400;600;700;800&display=swap">
<style>
:root{
  --blue:#1f7fc4;
  --blue-dark:#16639c;
  --navy:#1c2a3c;
  --navy-deep:#141e2b;
  --panel:#223349;
  --ink:#2b2f36;
  --muted:#7a808a;
  --line:#e3e6ea;
  --white:#ffffff;
  --teal:#23a7b5;
  --green:#7cb534;
  --indigo:#1e5b8f;
  --orange:#e2522c;
  --red:#d8312c;
}
*{box-sizing:border-box;margin:0;padding:0}
html,body{width:1200px;height:2972px;overflow:hidden}
body{font-family:"Open Sans",Arial,sans-serif;color:var(--ink);background:var(--white)}
a{color:inherit;text-decoration:none}

/* hero */
.hero{position:relative;height:792px;overflow:hidden}
.hero-photo{position:absolute;left:0;right:0;top:0;height:680px;background:linear-gradient(100deg,#e9eef3 0%,#c9d3dc 30%,#566a80 55%,#2b3a4e 75%,#1b2636 100%)}
.site-header{position:absolute;top:0;left:0;right:0;height:140px;display:flex;justify-content:space-between;padding:0 70px 0 20px}
.brand{margin-top:20px;display:flex;align-items:center;gap:12px;color:var(--white);font-weight:700;font-size:30px;background:rgba(20,30,43,.55);padding:14px 22px;height:78px}
.brand-mark{width:26px;height:26px;background:var(--blue)}
.main-nav{display:flex;gap:8px;margin-top:58px;height:46px}
.main-nav a{color:var(--white);font-size:15px;font-weight:600;letter-spacing:1px;padding:13px 22px}
.main-nav a.active{background:var(--blue)}
.hero-copy{position:absolute;left:100px;top:220px}
.hero-title{font-size:96px;font-weight:800;color:var(--blue);letter-spacing:5px;line-height:1}
.hero-sub{font-size:32px;font-weight:600;color:var(--white);letter-spacing:2px;margin:14px 0 0 60px}
.btn-outline{display:inline-block;border:2px solid var(--white);color:var(--white);font-size:18px;font-weight:600;letter-spacing:2px;padding:12px 32px}
.hero-copy .btn-outline{margin:38px 0 0 110px}

.partners{height:112px;background:var(--navy-deep);display:flex;align-items:center;padding:0 80px;gap:70px;position:absolute;left:0;right:0;bottom:0}
.partners-label{color:#8a96a6;font-size:15px;font-weight:600;letter-spacing:3px}
.partner-badge{width:170px;height:40px;background:#56677d;border-radius:4px}
.partner-badge.round{width:70px;border-radius:50%}

/* company info */
.company{height:480px;background:var(--panel);color:var(--white);text-align:center;padding-top:44px}
.section-title{font-size:34px;font-weight:700;letter-spacing:1px}
.company .section-title{margin-bottom:42px}
.info-row{display:flex;justify-content:center;gap:110px}
.info-item{width:250px}
.info-icon{width:120px;height:120px;border-radius:50%;background:var(--white);margin:0 auto 24px;display:flex;align-items:center;justify-content:center}
.info-item h3{font-size:22px;font-weight:700;margin-bottom:10px}
.info-item p{font-size:14px;line-height:1.45;color:#c9d2de}
.btn-small{display:inline-block;background:var(--blue);color:var(--white);font-size:14px;font-weight:700;padding:7px 26px;margin-top:20px}

/* services */
.services{height:548px;padding-top:56px;text-align:center}
.services .section-title{color:var(--ink)}
.services-intro{width:660px;margin:18px auto 48px;font-size:15px;line-height:1.5;color:var(--muted)}
.service-grid{display:grid;grid-template-columns:380px 380px;column-gap:150px;row-gap:56px;justify-content:center;text-align:left}
.service{display:flex;gap:22px}
.service-icon{width:90px;height:90px;flex:none;display:flex;align-items:center;justify-content:center}
.service h3{font-size:21px;font-weight:700;margin:2px 0 8px}
.service p{font-size:13px;line-height:1.5;color:var(--muted)}

/* testimonial */
.testimonial{position:relative;height:480px;text-align:center;color:var(--white);overflow:hidden}
.testimonial-photo{position:absolute;inset:0;background:linear-gradient(90deg,#3a4350 0%,#4d5866 45%,#2e3744 100%)}
.testimonial-body{position:relative;padding-top:86px}
.quote-mark{font-size:150px;font-weight:800;line-height:.8;height:90px}
.testimonial blockquote{width:780px;margin:30px auto 0;font-size:22px;font-weight:600;line-height:1.5}
.testimonial cite{display:block;font-style:normal;font-size:15px;color:#c8d0da;margin-top:22px}
.testimonial .btn-outline{margin-top:22px;font-size:17px;padding:10px 30px}

/* bottom columns */
.columns{height:488px;display:flex;justify-content:center;gap:70px;padding-top:32px}
.col{width:290px}
.col h2{font-size:22px;font-weight:700;letter-spacing:1px;padding-bottom:10px;border-bottom:2px solid var(--line);position:relative;margin-bottom:22px}
.col h2::after{content:"";position:absolute;left:0;bottom:-2px;width:60px;height:2px;background:var(--blue)}
.col-photo{height:130px;margin-bottom:18px}
.col h4{font-size:15px;color:var(--blue);font-weight:600;line-height:1.35;margin-bottom:8px}
.col p{font-size:12.5px;line-height:1.5;color:var(--muted);margin-bottom:10px}
.read-more{font-size:13px;color:var(--blue);font-weight:600}
.news-list{list-style:none}
.news-item{display:flex;gap:14px;margin-bottom:20px}
.news-date{width:52px;flex:none;text-align:center;color:var(--white)}
.news-date .day{display:block;background:var(--blue);font-size:20px;font-weight:700;padding:3px 0}
.news-date .month{display:block;background:var(--navy);font-size:11px;font-weight:700;padding:2px 0}
.news-item h5{font-size:13px;font-weight:700;color:var(--ink)}
.news-item p{margin:2px 0 0;font-size:11.5px;line-height:1.35}
.career-list{list-style:none;font-size:12.5px;color:var(--muted);line-height:1.7;margin-bottom:12px}

/* footer */
.site-footer{height:152px;background:var(--navy);display:flex;align-items:flex-start;padding:26px 120px 0 120px;gap:90px;color:#cfd6df}
.footer-links{list-style:none;font-size:12.5px;font-weight:600;line-height:2}
.footer-brand{margin-left:auto;display:flex;align-items:center;gap:12px;font-size:28px;font-weight:700;color:var(--white);margin-top:26px}
.copyright{height:32px;background:var(--blue-dark);color:#dbe7f3;font-size:12px;text-align:center;line-height:32px}
</style>
</head>
<body>

<section class="hero">
  <div class="hero-photo" role="img" aria-label="Photo of a businessman in a suit reviewing work on a tablet in a bright office"></div>
  <header class="site-header">
    <a class="brand" href="#"><span class="brand-mark"></span>Brindle Sky Advisory</a>
    <nav class="main-nav">
      <a class="active" href="#">HOME</a>
      <a href="#">ABOUT</a>
      <a href="#">SERVICES</a>
      <a href="#">PROJECTS</a>
      <a href="#">CONTACTS</a>
    </nav>
  </header>
  <div class="hero-copy">
    <h1 class="hero-title">SUCCEED!</h1>
    <p class="hero-sub">CHANGE YOUR FUTURE!</p>
    <a class="btn-outline" href="#">LEARN MORE</a>
  </div>
  <div class="partners">
    <span class="partners-label">OUR PARTNERS</span>
    <span class="partner-badge"></span>
    <span class="partner-badge"></span>
    <span class="partner-badge round"></span>
    <span class="partner-badge"></span>
  </div>
</section>

<section class="company">
  <h2 class="section-title">THE COMPANY INFORMATION</h2>
  <div class="info-row">
    <div class="info-item">
      <div class="info-icon">
        <svg width="70" height="70" viewBox="0 0 70 70"><circle cx="35" cy="35" r="30" fill="none" stroke="#1f7fc4" stroke-width="7"/><circle cx="35" cy="35" r="16" fill="none" stroke="#1c2a3c" stroke-width="6"/><circle cx="35" cy="35" r="5" fill="#1f7fc4"/><line x1="35" y1="35" x2="62" y2="8" stroke="#1c2a3c" stroke-width="4"/></svg>
      </div>
      <h3>NEW INFORMATION</h3>
      <p>We are committed to providing top service that is personal and tailored for each and every client. Meet the team at Harbor Point.</p>
      <a class="btn-small" href="#">MORE</a>
    </div>
    <div class="info-item">
      <div class="info-icon">
        <svg width="60" height="74" viewBox="0 0 60 74"><path d="M18 2h24l-6 12H24z" fill="#1c2a3c"/><path d="M24 16h12l8 40-14 16-14-16z" fill="#1f7fc4"/></svg>
      </div>
      <h3>WHAT WE DO?</h3>
      <p>We are committed to providing top service that is personal and tailored for each and every client. Meet the team at Harbor Point.</p>
      <a class="btn-small" href="#">MORE</a>
    </div>
    <div class="info-item">
      <div class="info-icon">
        <svg width="72" height="62" viewBox="0 0 72 62"><path d="M16 2h40l14 18-34 40L2 20z" fill="#d8312c"/><path d="M2 20h68M16 2l20 58M56 2L36 60M26 2l-6 18 16-18 16 18-6-18" fill="none" stroke="#f2a49a" stroke-width="2"/></svg>
      </div>
      <h3>WHY CHOOSE US</h3>
      <p>We are committed to providing top service that is personal and tailored for each and every client. Meet the team at Harbor Point.</p>
      <a class="btn-small" href="#">MORE</a>
    </div>
  </div>
</section>

<section class="services">
  <h2 class="section-title">OUR COMPANY SERVICES</h2>
  <p class="services-intro">Lorem ipsum dolor sit amet, consectetuer adipiscing elit. Praesent vestibulum molestie lacus. Aenean nonummy hendrerit mauris. Phasellus porta.</p>
  <div class="service-grid">
    <div class="service">
      <div class="service-icon" style="background:var(--teal)">
        <svg width="50" height="40" viewBox="0 0 50 40" fill="#fff"><circle cx="25" cy="10" r="8"/><path d="M11 38c0-10 6-16 14-16s14 6 14 16z"/><circle cx="9" cy="14" r="5"/><circle cx="41" cy="14" r="5"/><path d="M0 36c0-7 4-12 9-12s7 3 7 3l-5 9z M50 36c0-7-4-12-9-12s-7 3-7 3l5 9z"/></svg>
      </div>
      <div><h3>CONSULTING</h3><p>Lorem ipsum dolor sit amet, consectetuer adipiscing elit. Praesent vestibulum molestie lacus. Aenean nonummy hendrerit mauris. Phasellus porta.</p></div>
    </div>
    <div class="service">
      <div class="service-icon" style="background:var(--green)">
        <svg width="46" height="46" viewBox="0 0 46 46"><circle cx="23" cy="23" r="14" fill="none" stroke="#fff" stroke-width="8" stroke-dasharray="7 4"/><circle cx="23" cy="23" r="6" fill="#fff"/></svg>
      </div>
      <div><h3>TECHNOLOGY</h3><p>Lorem ipsum dolor sit amet, consectetuer adipiscing elit. Praesent vestibulum molestie lacus. Aenean nonummy hendrerit mauris. Phasellus porta.</p></div>
    </div>
    <div class="service">
      <div class="service-icon" style="background:var(--indigo)">
        <svg width="50" height="42" viewBox="0 0 50 42" fill="#fff"><rect x="2" y="2" width="46" height="30" rx="2"/><rect x="6" y="6" width="38" height="22" fill="#1e5b8f"/><rect x="18" y="34" width="14" height="4"/><rect x="12" y="38" width="26" height="3"/></svg>
      </div>
      <div><h3>INNOVATION</h3><p>Lorem ipsum dolor sit amet, consectetuer adipiscing elit. Praesent vestibulum molestie lacus. Aenean nonummy hendrerit mauris. Phasellus porta.</p></div>
    </div>
    <div class="service">
      <div class="service-icon" style="background:var(--orange)">
        <svg width="50" height="40" viewBox="0 0 50 40" fill="#fff"><path d="M4 14h10l22-12v36L14 26H4z"/><path d="M10 26h8l4 12h-8z"/><path d="M42 12q6 8 0 16" fill="none" stroke="#fff" stroke-width="3"/></svg>
      </div>
      <div><h3>MANAGEMENT</h3><p>Lorem ipsum dolor sit amet, consectetuer adipiscing elit. Praesent vestibulum molestie lacus. Aenean nonummy hendrerit mauris. Phasellus porta.</p></div>
    </div>
  </div>
</section>

<section class="testimonial">
  <div class="testimonial-photo" role="img" aria-label="Dimmed photo of a business team meeting around a table"></div>
  <div class="testimonial-body">
    <div class="quote-mark">&ldquo;</div>
    <blockquote>Lorem ipsum dolor sit amet, consectetuer adipiscing elit. Praesent vestibulum molestie lacus. Aenean nonummy hendrerit mauris. Phasellus porta.</blockquote>
    <cite>Dana Whitfield, our best specialist</cite>
    <a class="btn-outline" href="#">READ TESTIMONIALS</a>
  </div>
</section>

<section class="columns">
  <div class="col">
    <h2>ABOUT</h2>
    <div class="col-photo" role="img" aria-label="Photo of colleagues shaking hands in an office" style="background:linear-gradient(135deg,#dfe6ee,#9fb0c2)"></div>
    <h4>Does your business need Document Scanning?</h4>
    <p>Whether it's a bank, an office or a warehouse full of documents, we can provide you fast, safe and secure scanning.</p>
    <p>Whether it's a bank, an office or a warehouse full of documents.</p>
    <a class="read-more" href="#">Find out More...</a>
  </div>
  <div class="col">
    <h2>LATEST NEWS</h2>
    <ul class="news-list">
      <li class="news-item"><span class="news-date"><span class="day">29</span><span class="month">DEC</span></span><div><h5>Northwind - W25 Project</h5><p>Northwind review the W25 Project<br><a class="read-more" href="#">Read More...</a></p></div></li>
      <li class="news-item"><span class="news-date"><span class="day">14</span><span class="month">NOV</span></span><div><h5>Northwind Completes</h5><p>Northwind review the W25 Project<br><a class="read-more" href="#">Read More...</a></p></div></li>
      <li class="news-item"><span class="news-date"><span class="day">4</span><span class="month">OCT</span></span><div><h5>Northwind Expands Team</h5><p>Northwind review the W25 Project<br><a class="read-more" href="#">Read More...</a></p></div></li>
      <li class="news-item"><span class="news-date"><span class="day">25</span><span class="month">SEP</span></span><div><h5>Northwind - W23 Project</h5><p>Northwind review the W23 Project<br><a class="read-more" href="#">Read More...</a></p></div></li>
    </ul>
  </div>
  <div class="col">
    <h2>OUR CARRERS</h2>
    <div class="col-photo" role="img" aria-label="Photo of a group of young professionals together" style="background:linear-gradient(135deg,#e6ecf1,#a8b8c8)"></div>
    <h4>We're hiring!</h4>
    <p>Due to continued business growth we are actively looking for the right individuals for the following roles:</p>
    <ul class="career-list">
      <li>1. Technical Product Manager</li>
      <li>2. Senior Developer</li>
      <li>3. Senior Technical Consultant</li>
    </ul>
    <a class="read-more" href="#">Find out More...</a>
  </div>
</section>

<footer>
  <div class="site-footer">
    <ul class="footer-links"><li>HOME</li><li>ABOUT US</li><li>PRODUCTS</li><li>CAREER</li></ul>
    <ul class="footer-links"><li>CONTACT US</li><li>TERMS AND CONDITIONS</li><li>PRIVACY POLICY</li></ul>
    <div class="footer-brand"><span class="brand-mark"></span>Brindle Sky Advisory</div>
  </div>
  <div class="copyright">Copyright 2015 Brindle Sky Advisory. All rights reserved.</div>
</footer>

</body>
</html>
```